Create a packaging design for a new deodorant

New product container label. The jar is 2.75" in diameter and 2.75" high. The (transparent) label size is 1.5" by 8.5" and will wrap nearly fully around the jar when applied. Approximately 3.25" of the label will be devoted to the name and front section of the jar (what I am requesting you to design). Remaining part of the label will include a brief description, directions, general warning, ingredients, manufacturer, distributor, and barcode. The deodorant name is TOV. It is a clear colorless solution, ecologically friendly, naturally occurring deodorant salt solution. Water based, no alcohol, non-sticky, non-waxy, non-staining, just simple, clean and effective. Nature's way of getting the job done. Label to use transparent green and/or blue colors. Phrases such as " Fresh as a Springtime shower" or "Fresh as an ocean breeze" might be used. The deodorant has a NEW, unique, revolutionary applicator.

Target Market(s)

All adult men and women

Industry/Entity Type

Product

Number of Pages Required

1 page

Requirements
Nice to have
• TOV
• This is a new deodorant, a simple but elegant solution to an age-old problem.
• Why I Hate Deodorants
• I’ve had my share of problems with deodorants, and with antiperspirants for that matter, too. First off, the last thing I want to do when I step out of the shower is to put some sticky, slimy, or waxy goop on clean skin. I don’t like it when it feels like skin sticks together in skin folds. When I used to use the old stick deodorants, I would periodically scrape the edge of the plastic container against my skin and cause an abrasion that would then be irritated for the next 3 days. This would be particularly true when I got down to the bottom of the stick and the medication surface flattened out in the dispenser. Sometimes the deodorant or antiperspirant itself would cause such abrasions to grow red and angry and force me to stop using it altogether for the next week. Then I’d be hunting (and hurting) for alternatives. So every few months I would spend lots of time in the store looking at all the different brands of deodorants to find something that was a bit different - less caustic, less sticky, less stinky, or in a different dispenser that might work better for me. Roll-on deodorants work for me until they don’t. Half the time I’m trying to hold the bottle upside down and squeezing it so the product comes out. The other half of the time the roller ball gets stuck and I’m trying to get it to turn. What a waste of time. Or if it pours out, I have to spread it all over the place to get it thin enough to dry out. I dispensed with antiperspirants years ago when I had to throw away some of my favorite shirts because of sweat (really antiperspirant chemical) stains. I’ve also seen enough people with hidradenitis (infected sweat glands from using some antiperspirants) to know that some of these products that clog skin pores can be serious skin irritants.
• I’m a Natural Kind of Guy
• Don’t get me wrong. I’m not a tree hugger. I haven’t been out on the high seas in a rowboat maneuvering between a harpooner and a whale. But by the same token I don’t buy 3-step hair treatments. I don’t color my hair either. I don’t lounge around in bubble baths. And I don’t like to use heavy-scented cleansers, shampoos or skin products. I’m just looking for something clean, plain and simple ...something that works, that’s safe and dependable. Maybe even a natural product that has a long track record of safety and effectiveness.
• Just try it.....(There’s nothing more we’ll need to say!!)
• TOV uses a natural mineral salt, water, and a preservative. Nothing more. TOV has a unique and patented dispenser. The dispenser was made for the product and made for the job. One swipe application and you’re done! YOU can control the amount of deodorant applied by the sponge applicator. TOV is WATER-BASED. NO ALCOHOL. NO CHEMICALS. NO IRRITANTS. It dries quickly. No drips like you can get from spray bottles. The applicator doesn’t clog up or stop rolling. And it NEVER stains clothing. It’s just simple...easy...effective. And with a simple product we don’t have to charge a lot of money for it. So it’s inexpensive, too. I know you’re going to like this product.
• Swipe it on.... Odor gone!

```html
<!DOCTYPE html>
<html lang="en">
<head>
<meta charset="utf-8">
<title>TOV Deodorant – Spring Shower Label</title>
<link rel="stylesheet" href="https://fonts.googleapis.com/css2?family=Arimo:wght@400;700&family=Merienda:wght@700&display=swap">
<style>
  :root {
    --page-bg: #f2f3f1;
    --label-bg: #ffffff;
    --green-light: #6cc23a;
    --green-mid: #4e9a2c;
    --green-dark: #2f6a25;
    --rule-green: #5fae33;
    --body-grey: #7d817c;
  }
  * { box-sizing: border-box; margin: 0; padding: 0; }
  html, body {
    width: 1200px;
    height: 1000px;
    overflow: hidden;
    background: var(--page-bg);
  }
  .canvas {
    position: relative;
    width: 1200px;
    height: 1000px;
  }
  .label {
    position: absolute;
    left: 70px;
    top: 300px;
    width: 1060px;
    height: 400px;
    background: var(--label-bg);
    box-shadow: 0 2px 14px rgba(0,0,0,0.06);
  }
  .label__rule {
    position: absolute;
    left: 0;
    right: 0;
    height: 5px;
    background: var(--rule-green);
  }
  .label__rule--top { top: 18px; }
  .label__rule--bottom { bottom: 18px; }
  .side-copy {
    position: absolute;
    top: 50px;
    width: 230px;
    font-family: "Arimo", Arial, sans-serif;
    font-size: 13px;
    line-height: 23px;
    color: var(--body-grey);
  }
  .side-copy--left { left: 40px; text-align: left; }
  .side-copy--right { right: 40px; text-align: center; }
  .front {
    position: absolute;
    left: 280px;
    width: 500px;
    top: 50px;
    text-align: center;
  }
  .brand {
    font-family: "Arimo", Arial, sans-serif;
    font-weight: 700;
    font-size: 60px;
    line-height: 60px;
    letter-spacing: 2px;
    color: var(--green-dark);
  }
  .brand__category {
    font-family: "Arimo", Arial, sans-serif;
    font-weight: 400;
    font-size: 19px;
    line-height: 22px;
    letter-spacing: 0.5px;
    color: var(--green-dark);
  }
  .product-name {
    font-family: "Merienda", "Comic Sans MS", cursive;
    font-weight: 700;
    font-size: 52px;
    line-height: 70px;
    margin-top: 24px;
    white-space: nowrap;
  }
  .product-name__first { color: var(--green-light); }
  .product-name__second { color: var(--green-dark); }
  .claims {
    font-family: "Arimo", Arial, sans-serif;
    font-weight: 700;
    font-size: 12px;
    line-height: 17px;
    letter-spacing: 0.3px;
    color: var(--green-mid);
    text-transform: uppercase;
    margin-top: 34px;
  }
</style>
</head>
<body>
  <main class="canvas">
    <section class="label">
      <div class="label__rule label__rule--top"></div>

      <p class="side-copy side-copy--left">
        TOV is a clear, colorless mineral salt solution made with water and a gentle preservative. Nothing more. The new sponge applicator lets you control how much you use. One swipe and you are done. It dries quickly, never drips and never stains your favorite shirts. Swipe it on, odor gone.
      </p>

      <div class="front">
        <div class="brand">TOV</div>
        <div class="brand__category">DEODORANT</div>
        <h1 class="product-name">
          <span class="product-name__first">Spring</span>
          <span class="product-name__second">Shower</span>
        </h1>
        <p class="claims">Water based no alcohol non-sticky<br>non-waxy non-staining</p>
      </div>

      <p class="side-copy side-copy--right">
        Directions: apply one swipe to clean, dry skin after bathing. Use daily or as needed. Caution: for external use only. Do not apply to broken or irritated skin. Keep out of reach of children. Store with the lid closed in a cool place away from sunlight.
      </p>

      <div class="label__rule label__rule--bottom"></div>
    </section>
  </main>
</body>
</html>
```